Classic Car Web Banner Set Design

We need a set of banner ads designed for a manufacturing and retail company that sells weatherstripping for classic American vehicles (muscle cars, antique cars, classic cars). The banner ad must include our logo. There should be at least one car in the graphic, whole or partial. Our primary colors are Red and Black. Either a representation of auto weatherstripping or the words "Quality Weatherstripping" should be in the design.

Company name is "Harlow Gasket Works"

Sizes Needed: 300x250, 300x100, 728x90, 160x600, 120x90, 728x90, 234x60, 320x100, 750x100, 250x250

Target Market(s)

Consumer Audience, Classic Car Market

Industry/Entity Type

Retail

Font styles to use
Sans Serif

Colors
ec1f27

Requirements
Must have
• Red and Black primary colors. Company logo. Graphically show weatherstripping and/or automotive icons. If a vehicle is used, it must be an American vehicle.
Nice to have
• PSD files for selected entry.
Should not have
• no people

```html
<!DOCTYPE html>
<html lang="en">
<head>
<meta charset="utf-8">
<title>Harlow Gasket Works – Banner Set</title>
<link rel="stylesheet" href="https://fonts.googleapis.com/css2?family=Arimo:wght@400;700&display=swap">
<style>
  :root {
    --brand-red: #ec1f27;
    --ink: #000000;
    --paper: #ffffff;
    --label: #222222;
    --frame: #9a9a9a;
    --slate: #2b333b;
    --button-text: #5a3a00;
  }
  html, body {
    margin: 0;
    padding: 0;
    width: 1200px;
    height: 1200px;
    overflow: hidden;
    background: var(--paper);
    font-family: "Arimo", Arial, sans-serif;
  }
  .canvas { position: relative; width: 1200px; height: 1200px; }
  .banner { position: absolute; display: block; }
  .banner--leaderboard { left: 105px; top: 77px; }
  .banner--rectangle { left: 96px; top: 412px; }
  .banner--skyscraper { left: 898px; top: 298px; }
  .size-label {
    position: absolute;
    margin: 0;
    font-size: 19px;
    color: var(--label);
    text-align: center;
    width: 200px;
  }
  .size-label--leaderboard { left: 487px; top: 211px; }
  .size-label--rectangle { left: 203px; top: 777px; }
  .size-label--skyscraper { left: 910px; top: 1155px; }
  .brand-name { font-weight: 700; fill: var(--ink); }
  .headline { font-weight: 700; fill: var(--paper); }
  .cta-text { font-weight: 700; fill: var(--button-text); }
</style>
</head>
<body>
<main class="canvas">

  <svg width="0" height="0" style="position:absolute" aria-hidden="true">
    <defs>
      <radialGradient id="backdrop" cx="0.55" cy="0.35" r="0.8">
        <stop offset="0" stop-color="#808080"/>
        <stop offset="1" stop-color="#2e2e2e"/>
      </radialGradient>
      <radialGradient id="strip-photo" cx="0.5" cy="0.5" r="0.5">
        <stop offset="0" stop-color="#1c1c1c"/>
        <stop offset="0.6" stop-color="#262626" stop-opacity="0.95"/>
        <stop offset="1" stop-color="#3a3a3a" stop-opacity="0"/>
      </radialGradient>
      <radialGradient id="car-photo" cx="0.38" cy="0.6" r="0.62">
        <stop offset="0" stop-color="#6d3a5a"/>
        <stop offset="0.45" stop-color="#3d2734"/>
        <stop offset="0.8" stop-color="#262326" stop-opacity="0.85"/>
        <stop offset="1" stop-color="#2e2e2e" stop-opacity="0"/>
      </radialGradient>
      <linearGradient id="cta-fill" x1="0" y1="0" x2="0" y2="1">
        <stop offset="0" stop-color="#fff4a0"/>
        <stop offset="0.5" stop-color="#ffcc10"/>
        <stop offset="1" stop-color="#f2a300"/>
      </linearGradient>
    </defs>
  </svg>

  <!-- 728 x 90 leaderboard -->
  <svg class="banner banner--leaderboard" width="1015" height="126" viewBox="0 0 728 90" aria-label="Leaderboard banner">
    <rect x="0.5" y="0.5" width="727" height="89" fill="var(--paper)" stroke="var(--frame)"/>
    <text class="brand-name" x="73" y="41" font-size="17" text-anchor="middle">Harlow</text>
    <text class="brand-name" x="73" y="62" font-size="14" text-anchor="middle">Gasket Works</text>
    <path d="M152 1 Q136 45 152 89 H727 V1 Z" fill="var(--brand-red)"/>
    <path d="M161 1 Q147 45 161 89 H727 V1 Z" fill="var(--ink)"/>
    <path d="M404 1 Q448 40 434 89 H727 V1 Z" fill="url(#backdrop)"/>
    <path d="M404 1 Q448 40 434 89" fill="none" stroke="#d8d8d8" stroke-width="5"/>
    <ellipse cx="515" cy="58" rx="85" ry="34" fill="url(#car-photo)" role="img" aria-label="Photo of classic American muscle cars"/>
    <ellipse cx="555" cy="28" rx="55" ry="26" fill="url(#strip-photo)" role="img" aria-label="Photo of black rubber weatherstrip profile"/>
    <text class="headline" x="253" y="33" font-size="31" textLength="144" lengthAdjust="spacingAndGlyphs">QUALITY</text>
    <text class="headline" x="248" y="57" font-size="25" textLength="153" lengthAdjust="spacingAndGlyphs">WHEATHER</text>
    <text class="headline" x="253" y="82" font-size="25" textLength="144" lengthAdjust="spacingAndGlyphs">STRIPPING</text>
    <rect x="586" y="26" width="133" height="39" rx="19.5" fill="url(#cta-fill)" stroke="#fff" stroke-width="2"/>
    <text class="cta-text" x="652.5" y="51" font-size="14" text-anchor="middle">CLICK HERE!</text>
  </svg>
  <p class="size-label size-label--leaderboard">728X90</p>

  <!-- 300 x 250 medium rectangle -->
  <svg class="banner banner--rectangle" width="419" height="349" viewBox="0 0 300 250" aria-label="Medium rectangle banner">
    <rect x="0.5" y="0.5" width="299" height="249" fill="var(--paper)" stroke="var(--frame)"/>
    <text class="brand-name" x="150" y="33" font-size="17" text-anchor="middle">Harlow Gasket Works</text>
    <path d="M0.5 80 Q150 38 299.5 62 V249.5 H0.5 Z" fill="var(--brand-red)"/>
    <path d="M0.5 88 Q150 48 299.5 70 V228 Q150 244 0.5 214 Z" fill="var(--ink)"/>
    <path d="M184 60 Q160 150 178 238 H299.5 V70 Z" fill="url(#backdrop)"/>
    <path d="M184 60 Q160 150 178 238" fill="none" stroke="#d8d8d8" stroke-width="4"/>
    <path d="M0.5 226 Q150 252 299.5 234 V249.5 H0.5 Z" fill="var(--slate)"/>
    <ellipse cx="238" cy="178" rx="72" ry="44" fill="url(#car-photo)" role="img" aria-label="Photo of classic American muscle cars"/>
    <ellipse cx="236" cy="92" rx="58" ry="40" fill="url(#strip-photo)" role="img" aria-label="Photo of black rubber weatherstrip profile"/>
    <text class="headline" x="11" y="129" font-size="31" textLength="142" lengthAdjust="spacingAndGlyphs">QUALITY</text>
    <text class="headline" x="6" y="155" font-size="25" textLength="153" lengthAdjust="spacingAndGlyphs">WHEATHER</text>
    <text class="headline" x="11" y="180" font-size="25" textLength="142" lengthAdjust="spacingAndGlyphs">STRIPPING</text>
    <rect x="83" y="201" width="132" height="38" rx="19" fill="url(#cta-fill)" stroke="#fff" stroke-width="2"/>
    <text class="cta-text" x="149" y="225" font-size="14" text-anchor="middle">CLICK HERE!</text>
  </svg>
  <p class="size-label size-label--rectangle">300X250</p>

  <!-- 160 x 600 wide skyscraper -->
  <svg class="banner banner--skyscraper" width="224" height="840" viewBox="0 0 160 600" aria-label="Wide skyscraper banner">
    <rect x="0.5" y="0.5" width="159" height="599" fill="var(--paper)" stroke="var(--frame)"/>
    <text class="brand-name" x="80" y="40" font-size="17" text-anchor="middle">Harlow Gasket</text>
    <text class="brand-name" x="80" y="61" font-size="17" text-anchor="middle">Works</text>
    <path d="M0.5 100 Q80 74 159.5 100 V528 Q80 505 0.5 548 Z" fill="var(--brand-red)"/>
    <path d="M0.5 108 Q80 84 159.5 108 V228 Q118 300 0.5 308 Z" fill="var(--ink)"/>
    <path d="M0.5 308 Q118 300 159.5 228 V518 Q80 500 0.5 538 Z" fill="url(#backdrop)"/>
    <path d="M0.5 308 Q118 300 159.5 228" fill="none" stroke="#d8d8d8" stroke-width="4"/>
    <ellipse cx="80" cy="466" rx="92" ry="52" fill="url(#car-photo)" role="img" aria-label="Photo of classic American muscle cars"/>
    <ellipse cx="76" cy="360" rx="72" ry="58" fill="url(#strip-photo)" role="img" aria-label="Photo of black rubber weatherstrip profile"/>
    <text class="headline" x="80" y="153" font-size="30" text-anchor="middle" textLength="142" lengthAdjust="spacingAndGlyphs">QUALITY</text>
    <text class="headline" x="80" y="187" font-size="24" text-anchor="middle" textLength="152" lengthAdjust="spacingAndGlyphs">WHEATHER</text>
    <text class="headline" x="80" y="219" font-size="24" text-anchor="middle" textLength="144" lengthAdjust="spacingAndGlyphs">STRIPPING</text>
    <rect x="13" y="549" width="133" height="39" rx="19.5" fill="url(#cta-fill)" stroke="#fff" stroke-width="2"/>
    <text class="cta-text" x="79.5" y="574" font-size="14" text-anchor="middle">CLICK HERE!</text>
  </svg>
  <p class="size-label size-label--skyscraper">160X600</p>

</main>
</body>
</html>
```